Wavelume artwork for new single release

I need Wavelume artwork creating to release a new single on there.

The specs are:

Ideal size: 3000 x 3000 pixels
Minimum size: 1400 x 1400 pixels
Aspect ratio: 1:1 (must be a perfect square)
File format: JPG or PNG
Color space: sRGB
File size: Max 4MB

The song is called "Still, Can We Wander?"
The artist is "Milo Fenwright"

We have no images of Milo, so it really is open to imagination.

Target Market(s)

Wavelume listeners

Industry/Entity Type

Music

```html
<!DOCTYPE html>
<html lang="en">
<head>
<meta charset="utf-8">
<title>Milo Fenwright – Still, Can We Wander?</title>
<link rel="stylesheet" href="https://fonts.googleapis.com/css2?family=Montserrat:wght@700&family=Smokum&display=swap">
<style>
  :root {
    --bg-dark: #1b1b1a;
    --bg-mottle: #2a2a28;
    --ink-olive: #8b8668;
  }
  html, body {
    margin: 0;
    padding: 0;
    width: 1200px;
    height: 1200px;
    overflow: hidden;
    background: var(--bg-dark);
  }
  .cover {
    position: relative;
    width: 1200px;
    height: 1200px;
    background: var(--bg-dark);
  }
  .cover__texture,
  .cover__type {
    position: absolute;
    inset: 0;
    width: 1200px;
    height: 1200px;
  }
  .artist-name {
    font-family: "Montserrat", Arial, sans-serif;
    font-weight: 700;
    fill: var(--ink-olive);
  }
  .song-title {
    font-family: "Smokum", "Rye", serif;
    fill: var(--ink-olive);
  }
</style>
</head>
<body>
<main class="cover">
  <svg class="cover__texture" viewBox="0 0 1200 1200" aria-hidden="true">
    <defs>
      <filter id="mottle" x="0" y="0" width="100%" height="100%">
        <feTurbulence type="fractalNoise" baseFrequency="0.035" numOctaves="3" seed="7"/>
        <feColorMatrix type="matrix" values="0 0 0 0 0.17  0 0 0 0 0.17  0 0 0 0 0.16  0 0 0 1.6 -0.75"/>
      </filter>
    </defs>
    <rect width="1200" height="1200" fill="var(--bg-dark)"/>
    <rect width="1200" height="1200" filter="url(#mottle)"/>
  </svg>

  <svg class="cover__type" viewBox="0 0 1200 1200">
    <defs>
      <filter id="worn-ink">
        <feTurbulence type="fractalNoise" baseFrequency="0.9" numOctaves="2" seed="3" result="grain"/>
        <feColorMatrix in="grain" type="matrix" values="0 0 0 0 0  0 0 0 0 0  0 0 0 0 0  0 0 0 -9 6.2" result="holes"/>
        <feComposite in="SourceGraphic" in2="holes" operator="in"/>
      </filter>
    </defs>
    <text class="artist-name" x="336" y="308" font-size="62" letter-spacing="4"
          textLength="530" lengthAdjust="spacingAndGlyphs">MILO FENWRIGHT</text>
    <g class="song-title" filter="url(#worn-ink)">
      <text x="336" y="445" font-size="150" textLength="530" lengthAdjust="spacingAndGlyphs">STILL,</text>
      <text x="336" y="690" font-size="280" textLength="530" lengthAdjust="spacingAndGlyphs">CAN WE</text>
      <text x="336" y="937" font-size="280" textLength="530" lengthAdjust="spacingAndGlyphs">WANDER?</text>
    </g>
  </svg>
</main>
</body>
</html>
```